Stylish Homeware business needs a Logo and Business Card design

We need a logo and business card for a new company based in Hong Kong called "Nest Lumora". We do marketing and distributing international stylish Homeware brands in Asia. Products we handle included clocks, picture frame, small kitchen wares, LED lightenings, stationary and etc. We planned to also create our own brands next step. We could like to see designs that use pastel colors. The final design shoudl be simple and stylish.
Target Market(s)
Asia, Mainly Japan, China and Korea
Industry/Entity Type
Business
Contact Information for Business Card
We could like to see designs that use pastel colors. The final design shoudl be simple and stylish. We attach some log design we like on the bottom of the page.
Font styles to use
Look and feel
Each slider illustrates characteristics of the customer's brand and the style your logo design should communicate.

```html
<!DOCTYPE html>
<html lang="en">
<head>
<meta charset="UTF-8">
<title>Nest Lumora – Business Card</title>
<link href="https://fonts.googleapis.com/css2?family=Open+Sans:wght@400;700&family=Questrial&display=swap" rel="stylesheet">
<style>
  :root {
    --peach: #f5c2a2;
    --peach-deep: #d98b5f;
    --slate: #b9bfc9;
    --ink: #5b4f49;
    --text: #4a4643;
    --white: #ffffff;
    --bg: #f1efeb;
  }
  * { margin: 0; padding: 0; box-sizing: border-box; }
  html, body { width: 1200px; height: 900px; overflow: hidden; }
  body {
    background: var(--bg);
    font-family: "Open Sans", Arial, sans-serif;
    position: relative;
  }
  .card {
    position: absolute;
    left: 280px;
    width: 640px;
    height: 366px;
    box-shadow: 0 4px 14px rgba(0,0,0,0.10);
    overflow: hidden;
  }
  .card--back {
    top: 60px;
    background: var(--peach);
    display: flex;
    align-items: center;
    justify-content: center;
  }
  .card--front { top: 474px; background: var(--white); }

  .wordmark {
    font-family: "Questrial", Arial, sans-serif;
    font-weight: 400;
    letter-spacing: 4px;
    line-height: 1.05;
    text-transform: uppercase;
  }
  .card--back .wordmark {
    color: var(--white);
    font-size: 72px;
    text-shadow: none;
  }
  .card--back .wordmark { color: var(--ink); }
  .card--front .wordmark {
    position: absolute;
    color: var(--peach-deep);
    font-size: 54px;
    left: 352px;
    top: 108px;
  }

  .card-decor { position: absolute; inset: 0; width: 640px; height: 366px; }

  .person {
    position: absolute;
    left: 80px;
    top: 18px;
  }
  .person__name {
    color: var(--peach-deep);
    font-weight: 700;
    font-size: 17px;
    line-height: 22px;
  }
  .person__title {
    color: var(--text);
    font-size: 13px;
    line-height: 17px;
  }

  .contact {
    position: absolute;
    left: 48px;
    top: 140px;
    color: var(--text);
    font-size: 14.5px;
    line-height: 19px;
  }
  .contact__address { margin-left: 20px; margin-bottom: 2px; }
  .contact__row { display: flex; align-items: center; gap: 8px; }
  .contact__row svg { width: 12px; height: 12px; flex: none; }
</style>
</head>
<body>

  <section class="card card--back">
    <div class="wordmark">Nest<br>Lumora</div>
  </section>

  <section class="card card--front">
    <svg class="card-decor" viewBox="0 0 640 366" aria-hidden="true">
      <polygon points="0,0 34,0 0,34" fill="var(--peach)"/>
      <polygon points="40,0 64,0 48,42 14,42" fill="var(--slate)"/>
      <polygon points="0,262 318,262 304,286 0,286" fill="var(--peach)"/>
      <polygon points="316,292 640,292 640,336 292,336" fill="var(--slate)"/>
    </svg>

    <div class="person">
      <div class="person__name">Daniel Hartley</div>
      <div class="person__title">Managing Director</div>
    </div>

    <div class="wordmark">Nest<br>Lumora</div>

    <div class="contact">
      <div class="contact__address">18 Harbour View Road<br>Hong Kong, 999077.</div>
      <div class="contact__row">
        <svg viewBox="0 0 12 12" aria-hidden="true"><path d="M2.5 1 L4.5 1 L5.2 3.6 L4 4.6 Q5 7 7.4 8 L8.4 6.8 L11 7.5 L11 9.5 Q10.5 11 9 11 Q1 10.2 1 2.6 Q1 1 2.5 1 Z" fill="var(--peach-deep)"/></svg>
        <span>852-2345 6781</span>
      </div>
      <div class="contact__row">
        <svg viewBox="0 0 12 12" aria-hidden="true"><rect x="0.5" y="2.5" width="11" height="7.5" fill="var(--peach-deep)"/><polyline points="0.8,2.8 6,7 11.2,2.8" fill="none" stroke="var(--white)" stroke-width="1"/></svg>
        <span>hello@nestlumora.com</span>
      </div>
      <div class="contact__row">
        <svg viewBox="0 0 12 12" aria-hidden="true"><circle cx="6" cy="6" r="5.5" fill="var(--peach-deep)"/><path d="M0.5 6 H11.5 M6 0.5 Q2.5 6 6 11.5 M6 0.5 Q9.5 6 6 11.5" fill="none" stroke="var(--white)" stroke-width="0.8"/></svg>
        <span>www.nestlumora.com</span>
      </div>
    </div>
  </section>

</body>
</html>
```